We are looking for a 2-page (front and back) 3.67" x 8.5" rack card. . Please refer back to our other Rack Cards for a similar look and feel to the card. This one is titled: Myths and Truths About Memory Loss
The document is for older readers. Do not put text over graphics and keep it simple and easy to read with high contrast.
We want some very simple design element(s) incorporated that convey Native American communities or heritage. But NO headdress, teepee graphics, owls etc. I have included some graphics, please use your creative discretion to use which ones look good on the cards. Please remember to include the funding statement - it can be in a very small font 6/7 point. For more information about our project, please visit https://orvelmesa.net/mind-care/library - This rack card is supported by the Bureau for Wellness Tracking and Outreach (BWT) of the Federal Office of Family and Care Affairs (FOF) as part of a financial assistance award totaling $874,260.00 with 100 percent funded by BWT/FOF. The contents are those of the author(s) and do not necessarily represent the official views of, nor an endorsement, by BWT/FOF, or the the Northwind Commonwealth.
Please feel free to choose one of each of the 2 logos that looks best. We have the QT7 logo and the Mind Wellness Support Hub logo we would like to add. I have added the document and there are images to choose from to use in the rack card. We definitely want to incorporate the coyote in this rack card since it is culturally significant.

```html
<!DOCTYPE html>
<html lang="en">
<head>
<meta charset="utf-8">
<title>Myths and Truths About Memory Loss – Rack Card</title>
<link rel="stylesheet" href="https://fonts.googleapis.com/css2?family=Oswald:wght@500;600;700&family=Open+Sans:wght@400;600;700;800&display=swap">
<style>
  :root{
    --teal:#3a9fab;
    --teal-dark:#2b7f89;
    --maroon:#7b2b2b;
    --maroon-dark:#5e1f1f;
    --cream:#f6f1e8;
    --ink:#3b2c27;
    --paper:#ffffff;
    --stage:#e9e9ea;
    --rule:#c9b8a6;
  }
  *{box-sizing:border-box;margin:0;padding:0}
  html,body{width:698px;height:1200px;overflow:hidden;background:var(--stage)}
  body{font-family:"Open Sans",Arial,sans-serif;color:var(--ink)}
  .sheet{position:relative;width:698px;height:1200px;display:flex;gap:14px;justify-content:center;align-items:center}
  .card{position:relative;width:330px;height:764px;background:var(--paper);overflow:hidden;display:flex;flex-direction:column;box-shadow:0 2px 8px rgba(0,0,0,.15)}

  /* front */
  .brand{display:flex;align-items:center;gap:8px;padding:16px 16px 8px}
  .brand-mark{width:34px;height:34px;background:var(--teal);flex:none}
  .brand-name{font-family:"Oswald",sans-serif;font-weight:700;font-size:30px;color:var(--maroon);line-height:1}
  .brand-tag{font-family:"Oswald",sans-serif;font-weight:600;font-size:10.5px;color:var(--maroon);line-height:1.15;letter-spacing:.3px;text-transform:uppercase}
  .hero{position:relative;height:178px;flex:none}
  .hero-band{position:absolute;inset:0;width:100%;height:100%}
  .pattern-strip{position:absolute;left:0;right:0;height:10px;background:linear-gradient(90deg,var(--maroon),#a45b4a 50%,var(--maroon))}
  .photo-circle{position:absolute;border-radius:50%;border:4px solid var(--paper);box-shadow:0 0 0 2px var(--teal)}
  .photo-elders{left:62px;top:8px;width:150px;height:150px;background:radial-gradient(circle at 40% 40%,#c7654d,#7a3a2d 70%,#4f2a22)}
  .photo-elder{left:196px;top:66px;width:108px;height:108px;background:radial-gradient(circle at 50% 45%,#d9b79a,#9e7058 60%,#6b8a5c)}
  .title{font-family:"Oswald",sans-serif;font-weight:700;color:var(--maroon);text-align:center;font-size:31px;line-height:1.02;letter-spacing:.4px;text-transform:uppercase;padding:12px 14px 6px}
  .intro{font-size:9.6px;line-height:1.42;text-align:center;padding:0 22px 10px}

  .mvt{margin:0 14px}
  .mvt-head{display:grid;grid-template-columns:1fr auto 1fr;align-items:center;background:var(--teal);color:#fff;font-family:"Oswald",sans-serif;font-weight:700;font-size:15px;letter-spacing:.5px;padding:3px 10px}
  .mvt-head .vs{font-size:11px;padding:0 6px}
  .mvt-head .truth-label{text-align:right}
  .mvt-row{display:grid;grid-template-columns:1fr 1fr;border-bottom:1px solid var(--rule)}
  .mvt-row:last-child{border-bottom:0}
  .myth,.truth{font-size:9.3px;line-height:1.38;padding:7px 8px 7px 14px;position:relative}
  .myth{font-weight:700;color:var(--maroon-dark);border-right:2px solid var(--teal)}
  .myth::before,.truth::before{content:"";position:absolute;left:5px;top:11px;width:4px;height:4px;border-radius:50%;background:var(--teal)}
  .truth::before{background:var(--maroon)}

  .quote-band{margin-top:auto;position:relative;background:var(--teal);color:#fff;padding:18px 22px 14px;text-align:center}
  .quote-band .pattern-strip{top:0}
  .quote{font-size:10px;font-style:italic;line-height:1.4}
  .quote-by{font-size:7.5px;margin-top:4px;opacity:.9}

  /* back */
  .photo-textiles{height:206px;flex:none;background:linear-gradient(100deg,#6e2a24,#b8543f 25%,#2f4d63 45%,#c89b52 65%,#7b2b2b 85%,#3c2a22)}
  .back .pattern-strip.under{position:static;flex:none}
  .back .mvt{margin-top:12px}
  .section-band{margin:12px 14px 0;background:var(--maroon);color:#fff;font-family:"Oswald",sans-serif;font-weight:700;font-size:16px;letter-spacing:.6px;text-align:center;padding:3px 0}
  .todo{font-size:9.6px;line-height:1.42;text-align:center;padding:7px 22px 0}
  .resources{margin:10px 14px 0;background:var(--cream);border-left:4px solid var(--teal);padding:8px 10px}
  .resources h3{font-family:"Oswald",sans-serif;font-weight:700;font-size:12px;color:var(--maroon);letter-spacing:.3px;margin-bottom:4px}
  .resource{font-size:8.6px;line-height:1.3;margin-bottom:4px}
  .resource:last-child{margin-bottom:0}
  .resource b{color:var(--maroon-dark)}
  .resource .url{color:var(--teal-dark);word-break:break-all}
  .funding{padding:7px 16px 8px;font-size:6.6px;line-height:1.35}
  .funding b{color:var(--maroon);font-size:7.4px}
  .back-foot{margin-top:auto;position:relative;background:var(--teal);color:#fff;padding:16px 14px 10px;display:flex;align-items:center;gap:10px;flex:none}
  .back-foot .pattern-strip{top:0}
  .back-foot p{font-size:8.4px;line-height:1.35;flex:1}
  .hub{display:flex;align-items:center;gap:5px;font-weight:800;font-size:8.4px;line-height:1.1;width:96px;flex:none}
  .hub-dot{width:16px;height:16px;border-radius:50%;background:#fff;flex:none}
</style>
</head>
<body>
<main class="sheet">

  <section class="card front">
    <header class="brand">
      <span class="brand-mark"></span>
      <span class="brand-name">QT7</span>
      <span class="brand-tag">International Alliance for<br>Tribal Elder Care</span>
    </header>

    <div class="hero">
      <svg class="hero-band" viewBox="0 0 330 178" preserveAspectRatio="none" aria-hidden="true">
        <polygon points="0,60 330,20 330,130 0,170" fill="#3a9fab"/>
        <polygon points="0,54 330,14 330,22 0,62" fill="#7b2b2b"/>
        <polygon points="0,168 330,128 330,136 0,176" fill="#7b2b2b"/>
      </svg>
      <div class="photo-circle photo-elders" role="img" aria-label="Photo of a Native Elder in a traditional patterned shawl"></div>
      <div class="photo-circle photo-elder" role="img" aria-label="Photo of a smiling Native Elder outdoors"></div>
    </div>

    <h1 class="title">Myths and Truths<br>About Memory Loss</h1>
    <p class="intro">People sometimes believe things about memory loss that are not true. Misunderstandings can make it harder for Elders in Native communities to get the help they need when they start having memory issues. Below are some common myths and truths about memory loss, Alzheimer's disease, and related dementias.</p>

    <div class="mvt">
      <div class="mvt-head"><span>MYTH</span><span class="vs">VS.</span><span class="truth-label">TRUTH</span></div>
      <div class="mvt-row">
        <p class="myth">Getting Alzheimer's is a normal part of aging.</p>
        <p class="truth">It is a disease that not everyone will get.</p>
      </div>
      <div class="mvt-row">
        <p class="myth">Memory problems and forgetfulness are definite signs of dementia.</p>
        <p class="truth">Memory problems do not solely determine if they are dementia. Other medical conditions can cause memory problems. Talk to your doctor.</p>
      </div>
      <div class="mvt-row">
        <p class="myth">Only older people can get Alzheimer's disease.</p>
        <p class="truth">There have been cases for people as young as their 30s.</p>
      </div>
    </div>

    <footer class="quote-band">
      <div class="pattern-strip" role="img" aria-label="Woven zigzag border pattern"></div>
      <p class="quote">"The beauty in life is being able to be your true self, and a better version of myself than yesterday."</p>
      <p class="quote-by">— Community Elder, Wellness Circle Gathering</p>
    </footer>
  </section>

  <section class="card back">
    <div class="photo-textiles" role="img" aria-label="Photo of colorful woven Native textiles and blankets"></div>
    <div class="pattern-strip under" role="img" aria-label="Woven zigzag border pattern"></div>

    <div class="mvt">
      <div class="mvt-head"><span>MYTH</span><span class="vs">VS.</span><span class="truth-label">TRUTH</span></div>
      <div class="mvt-row">
        <p class="myth">People with Alzheimer's disease cannot be happy.</p>
        <p class="truth">A person with memory loss can experience strong moods and emotions but still enjoy life and relationships.</p>
      </div>
      <div class="mvt-row">
        <p class="myth">Dementia can be prevented by a certain supplement or food.</p>
        <p class="truth">Healthy eating may help overall wellness, including brain health. No additional supplements will completely prevent the onset of dementia.</p>
      </div>
      <div class="mvt-row">
        <p class="myth">Alzheimer's is reversible through prescription drugs.</p>
        <p class="truth">There are prescription drugs to alleviate symptoms of Alzheimer's and dementia, but there are no medicines that can reverse them.</p>
      </div>
    </div>

    <h2 class="section-band">WHAT YOU CAN DO</h2>
    <p class="todo">If you or someone you love is having memory problems, do not wait. Talk to a healthcare provider you trust. Learning the truth can help keep our Elders strong and supported.</p>

    <div class="resources">
      <h3>FOR MORE MYTH-BUSTING INFORMATION:</h3>
      <p class="resource"><b>10 Common Alzheimer's Disease Myths on HomeHelper Hub</b><br><span class="url">www.homehelperhub.com/guides/memory-myths</span></p>
      <p class="resource"><b>Memory Care Society Myths vs. Facts</b><br><span class="url">www.memorycaresociety.org/learn/myths-and-facts</span></p>
      <p class="resource"><b>QT7 Brain Health Resources</b><br><span class="url">https://orvelmesa.net/mind-care/library</span></p>
    </div>

    <p class="funding"><b>FUNDING STATEMENT:</b><br>This rack card is supported by the Bureau for Wellness Tracking and Outreach (BWT) of the Federal Office of Family and Care Affairs (FOF) as part of a financial assistance award totaling $874,260.00 with 100 percent funded by BWT/FOF. The contents are those of the author(s) and do not necessarily represent the official views of, nor an endorsement, by BWT/FOF, or the Northwind Commonwealth.</p>

    <footer class="back-foot">
      <div class="pattern-strip" role="img" aria-label="Woven zigzag border pattern"></div>
      <p>For more information about our project, please visit https://orvelmesa.net/mind-care/library</p>
      <div class="hub"><span class="hub-dot"></span><span>Mind Wellness Support Hub</span></div>
    </footer>
  </section>

</main>
</body>
</html>
```